New Business Card Design for Engineering and Surveying Company

We need a new design template for our business cards. We are a civil engineering, land surveying and pipeline integrity business. Please see brqholt.com for details. We need a bold, new business card design to complement our rebranding and marketing program. We have anew logo and attached vectro file. Please find additional details below. I am available to answer any questions.

Target Market(s)

Contractors, business owners, oil companies

Contact Information for Business Card

Needs to be customizable for different people (name, title, cell)

Font styles to use
Sans Serif
Other font styles liked:
• See eps file

Requirements
Must have
• Example Information:
Derek Fannaby

T:409-555-0187
M: 202-555-0143
dfannaby@brqholt.com

Address: 1870 Corvane Parkway, Beaumont, Texas 77701
Email: dfanbagy@brqholt.com
Website: www.brqholt.com
Nice to have
• I would like the back of the card to have the logo on a bold background with the text below:

[logo]
ROLAND FANNABY & ASSOCIATES
CIVIL ENGINEERING | LAND SURVEYING | PIPELINE INTEGRITY

The reverse side should have the contact information for the person (example above), a smaller version of the logo and a graphic

```html
<!DOCTYPE html>
<html lang="en">
<head>
<meta charset="utf-8">
<title>Roland Fannaby &amp; Associates — Business Card</title>
<link rel="stylesheet" href="https://fonts.googleapis.com/css2?family=Montserrat:wght@500;600;700;800&display=swap">
<style>
  :root {
    --brand-blue: #1c53a8;
    --brand-red: #e51b2d;
    --name-red: #a8141e;
    --ink: #0b0f18;
    --text: #2f2f33;
    --card-white: #ffffff;
    --backdrop: #e9eaed;
  }
  * { margin: 0; padding: 0; box-sizing: border-box; }
  html, body {
    width: 1200px; height: 1000px; overflow: hidden;
    background: var(--backdrop);
    font-family: "Montserrat", Arial, sans-serif;
  }
  .sheet {
    width: 1200px; height: 1000px;
    display: flex; flex-direction: column; align-items: center; justify-content: center;
    gap: 50px;
  }
  .card {
    width: 700px; height: 400px; border-radius: 34px;
    position: relative; overflow: hidden;
    box-shadow: 0 10px 28px rgba(0,0,0,.18);
  }

  /* Back side */
  .card--back { background: var(--brand-blue); color: #fff; }
  .back-brand {
    position: absolute; top: 120px; left: 0; right: 0;
    display: flex; flex-direction: column; align-items: center; gap: 26px;
  }
  .brand-mark {
    width: 46px; height: 46px; background: var(--brand-red); border-radius: 50%;
  }
  .back-brand__name {
    font-weight: 800; font-size: 34px; letter-spacing: 1.5px; white-space: nowrap;
  }
  .services {
    position: absolute; bottom: 62px; left: 0; right: 0;
    display: flex; justify-content: center; gap: 30px;
    list-style: none; font-weight: 500; font-size: 17px; letter-spacing: 1px;
  }
  .services li { display: flex; align-items: center; gap: 10px; }
  .services li::before {
    content: ""; width: 9px; height: 9px; border-radius: 50%; background: var(--brand-red);
  }

  /* Front side */
  .card--front { background: var(--card-white); }
  .front-brand {
    position: absolute; top: 62px; right: 48px;
    display: flex; align-items: center; gap: 14px;
  }
  .front-brand .brand-mark { width: 34px; height: 34px; }
  .front-brand__name {
    font-weight: 800; font-size: 22px; letter-spacing: .5px; color: var(--ink); white-space: nowrap;
  }
  .person {
    position: absolute; top: 150px; left: 0; padding-left: 56px;
  }
  .person__accent {
    position: absolute; left: 0; top: 2px; width: 30px; height: 52px; background: var(--name-red);
  }
  .person__name {
    font-weight: 800; font-size: 30px; color: var(--name-red); letter-spacing: .5px;
  }
  .person__title {
    font-weight: 600; font-size: 18px; color: var(--brand-blue); letter-spacing: .8px; margin-top: 2px;
  }
  .contacts {
    position: absolute; top: 262px; left: 56px; list-style: none;
    font-weight: 500; font-size: 17px; color: var(--text); letter-spacing: .6px;
  }
  .contacts li { display: flex; align-items: center; gap: 12px; height: 26px; }
  .contacts svg { width: 15px; height: 15px; fill: var(--brand-blue); flex: none; }
  .address {
    position: absolute; right: 48px; bottom: 50px;
    display: flex; align-items: stretch; gap: 14px;
  }
  .address__text {
    font-style: normal; font-weight: 500; font-size: 18px; color: var(--text);
    text-align: right; line-height: 1.45; letter-spacing: .6px;
  }
  .address__rule { width: 4px; background: var(--brand-red); }
</style>
</head>
<body>
<main class="sheet">
  <section class="card card--back" aria-label="Card back">
    <div class="back-brand">
      <span class="brand-mark" aria-hidden="true"></span>
      <h1 class="back-brand__name">ROLAND FANNABY &amp; ASSOCIATES</h1>
    </div>
    <ul class="services">
      <li>CIVIL ENGINEERING</li>
      <li>LAND SURVEYING</li>
      <li>PIPELINE INTEGRITY</li>
    </ul>
  </section>

  <section class="card card--front" aria-label="Card front">
    <div class="front-brand">
      <span class="brand-mark" aria-hidden="true"></span>
      <span class="front-brand__name">ROLAND FANNABY &amp; ASSOCIATES</span>
    </div>

    <div class="person">
      <span class="person__accent" aria-hidden="true"></span>
      <h2 class="person__name">DEREK FANNABY</h2>
      <p class="person__title">Managing Director</p>
    </div>

    <ul class="contacts">
      <li>
        <svg viewBox="0 0 24 24" aria-hidden="true"><path d="M6.6 10.8a15 15 0 0 0 6.6 6.6l2.2-2.2c.3-.3.7-.4 1-.2 1.1.4 2.3.6 3.6.6.6 0 1 .4 1 1V20c0 .6-.4 1-1 1A17 17 0 0 1 3 4c0-.6.4-1 1-1h3.5c.6 0 1 .4 1 1 0 1.3.2 2.5.6 3.6.1.3 0 .7-.2 1z"/></svg>
        409-555-0187
      </li>
      <li>
        <svg viewBox="0 0 24 24" aria-hidden="true"><path d="M7 1h10a2 2 0 0 1 2 2v18a2 2 0 0 1-2 2H7a2 2 0 0 1-2-2V3a2 2 0 0 1 2-2zm0 3v14h10V4zm5 15.5a1.2 1.2 0 1 0 0 2.4 1.2 1.2 0 0 0 0-2.4z"/></svg>
        202-555-0143
      </li>
      <li>
        <svg viewBox="0 0 24 24" aria-hidden="true"><path d="M2 5h20v14H2zm2 2v.5l8 5 8-5V7zm0 2.8V17h16V9.8l-8 5z"/></svg>
        dfannaby@brqholt.com
      </li>
      <li>
        <svg viewBox="0 0 24 24" aria-hidden="true"><path d="M12 2a10 10 0 1 0 0 20 10 10 0 0 0 0-20zm-1 17.9A8 8 0 0 1 4 12l5 5v1a2 2 0 0 0 2 2zm6.9-2.5A2 2 0 0 0 16 16h-1v-3a1 1 0 0 0-1-1H8v-2h2a1 1 0 0 0 1-1V7h2a2 2 0 0 0 2-2v-.4a8 8 0 0 1 2.9 12.8z"/></svg>
        www.brqholt.com
      </li>
    </ul>

    <div class="address">
      <address class="address__text">1870 Corvane Parkway<br>Beaumont, Texas 77701</address>
      <span class="address__rule" aria-hidden="true"></span>
    </div>
  </section>
</main>
</body>
</html>
```